Convert Design into Adobe Ilustrator (Ai) File - Product Label

Convert the provided Graphic Design into an Adobe Illustrator (Ai) File for a Product Label. This Ai file needs to be fully editable, organised into logical layers and well structured. The text needs to be outlined for printing. This is for a POUCH DESIGN. The pouch dimensions file is attached. We'll share the details for the other side of the pouch if you are interested in accepting this project. Thanks.

Industry/Entity Type

FOOD SUPPLEMENTS

```html
<!DOCTYPE html>
<html lang="en">
<head>
<meta charset="utf-8">
<title>Meridian &amp; Mind – Marine Collagen Complex Pouch Dieline</title>
<link rel="stylesheet" href="https://fonts.googleapis.com/css2?family=Arimo:wght@400;700&family=Cormorant+Garamond:wght@400;500&family=Crimson+Text&display=swap">
<style>
  :root {
    --paper: #ffffff;
    --title-red: #e8202a;
    --title-blue: #2e3192;
    --navy-light: #263d62;
    --navy-dark: #121b2e;
    --gold: #d9a676;
    --ink-light: #e4e8ef;
    --guide-blue: #2aa6e0;
    --dim-ink: #111111;
  }
  * { margin: 0; padding: 0; box-sizing: border-box; }
  html, body { width: 1200px; height: 840px; overflow: hidden; background: var(--paper); }
  .sheet { position: relative; width: 1200px; height: 840px; }
  .sheet-title {
    position: absolute; left: 0; top: 24px; width: 1200px; text-align: center;
    font-family: "Arimo", Arial, sans-serif; font-weight: 700; line-height: 1;
  }
  .sheet-title .kicker { display: block; font-size: 31px; color: var(--title-red); }
  .sheet-title .headline { display: block; font-size: 43px; color: var(--title-red); margin-top: 6px; }
  .sheet-title .headline em { font-style: normal; color: var(--title-blue); }
  .dieline { position: absolute; left: 0; top: 0; }
  .dim-text { font-family: "Arimo", Arial, sans-serif; fill: var(--dim-ink); }
  .dim-line { stroke: var(--dim-ink); stroke-width: 0.8; fill: none; }
  .guide { stroke: var(--guide-blue); stroke-width: 1; stroke-dasharray: 4 3; fill: none; }
  .brand { font-family: "Cormorant Garamond", serif; font-weight: 500; fill: var(--gold); letter-spacing: 0.22em; }
  .product-name { font-family: "Cormorant Garamond", serif; font-weight: 400; fill: var(--gold); letter-spacing: 0.14em; }
  .body-copy { font-family: "Crimson Text", "Times New Roman", serif; fill: var(--ink-light); }
  .icon { stroke: var(--ink-light); stroke-width: 0.8; fill: none; }
</style>
</head>
<body>
<main class="sheet">
  <h1 class="sheet-title">
    <span class="kicker">All Four Side Round Corner</span>
    <span class="headline">Stand Up Pouch <em>With Zipper</em></span>
  </h1>

  <svg class="dieline" width="1200" height="840" viewBox="0 0 1200 840">
    <defs>
      <linearGradient id="pouch-fill" x1="0" y1="0" x2="1" y2="1">
        <stop offset="0" stop-color="var(--navy-light)"/>
        <stop offset="1" stop-color="var(--navy-dark)"/>
      </linearGradient>
      <linearGradient id="contour-fill" x1="0" y1="0" x2="0" y2="1">
        <stop offset="0" stop-color="#3a5277" stop-opacity="0"/>
        <stop offset="1" stop-color="#3a5277" stop-opacity="0.35"/>
      </linearGradient>
    </defs>

    <!-- dimension annotations -->
    <g class="dimensions">
      <text class="dim-text" x="378" y="116" font-size="11" text-anchor="middle">8mm</text>
      <text class="dim-text" x="378" y="130" font-size="11" text-anchor="middle">Seal</text>
      <text class="dim-text" x="822" y="116" font-size="11" text-anchor="middle">8mm</text>
      <text class="dim-text" x="822" y="130" font-size="11" text-anchor="middle">Seal</text>
      <text class="dim-text" x="601" y="160" font-size="19" text-anchor="middle">Total Width_190mm</text>
      <text class="dim-text" x="601" y="179" font-size="15.5" text-anchor="middle">174mm</text>
      <line class="dim-line" x1="369" y1="165" x2="831" y2="165"/>
      <line class="dim-line" x1="384" y1="180" x2="816" y2="180"/>
      <line class="dim-line" x1="369" y1="158" x2="369" y2="190"/>
      <line class="dim-line" x1="831" y1="158" x2="831" y2="190"/>
      <line class="dim-line" x1="379" y1="134" x2="379" y2="186"/>
      <line class="dim-line" x1="821" y1="134" x2="821" y2="186"/>

      <line class="dim-line" x1="857" y1="196" x2="857" y2="829"/>
      <line class="dim-line" x1="841" y1="196" x2="867" y2="196"/>
      <line class="dim-line" x1="841" y1="256" x2="867" y2="256"/>
      <line class="dim-line" x1="841" y1="288" x2="867" y2="288"/>
      <line class="dim-line" x1="841" y1="829" x2="867" y2="829"/>
      <text class="dim-text" font-size="15" transform="translate(863 226) rotate(90)" text-anchor="middle">25mm</text>
      <line class="dim-line" x1="852" y1="271" x2="890" y2="271"/>
      <path d="M890 271 l-5 -3 v6 z" fill="var(--dim-ink)"/>
      <text class="dim-text" x="895" y="266" font-size="13">13mm</text>
      <text class="dim-text" x="895" y="282" font-size="13">Zipper</text>
      <text class="dim-text" font-size="19" transform="translate(866 575) rotate(90)" text-anchor="middle">222mm</text>
    </g>

    <!-- pouch front -->
    <g class="pouch-front" transform="translate(369 196)">
      <rect width="463" height="634" rx="6" fill="url(#pouch-fill)"/>
      <rect y="330" width="463" height="304" rx="6" fill="url(#contour-fill)" role="img" aria-label="Fine gold and slate contour-line wave pattern across the lower half"/>

      <line class="guide" x1="15.5" y1="0" x2="15.5" y2="634"/>
      <line class="guide" x1="447.5" y1="0" x2="447.5" y2="634"/>
      <line class="guide" x1="0" y1="60" x2="463" y2="60"/>
      <line class="guide" x1="0" y1="93" x2="463" y2="93"/>
      <circle cx="3" cy="48" r="2" fill="var(--guide-blue)"/>
      <circle cx="460" cy="48" r="2" fill="var(--guide-blue)"/>
      <line class="guide" x1="0" y1="499" x2="21" y2="499"/>
      <line class="guide" x1="447" y1="499" x2="463" y2="499"/>
      <path class="guide" d="M21 499 C 70 640, 390 640, 447 499"/>

      <line x1="191" y1="33" x2="275" y2="33" stroke="var(--gold)" stroke-width="0.8"/>
      <circle cx="232" cy="33" r="20" fill="var(--navy-light)" stroke="var(--gold)" stroke-width="1.4"/>

      <text class="brand" x="242" y="148" font-size="22" text-anchor="middle">MERIDIAN &amp; MIND</text>
      <line x1="58" y1="183" x2="409" y2="183" stroke="var(--gold)" stroke-width="0.7"/>

      <text class="product-name" font-size="37">
        <tspan x="58" y="245">MARINE</tspan>
        <tspan x="58" y="276">COLLAGEN</tspan>
        <tspan x="58" y="307">COMPLEX</tspan>
      </text>

      <text class="body-copy" font-size="17">
        <tspan x="58" y="401">Marine Collagen,</tspan>
        <tspan x="58" y="419">Vitamin C</tspan>
        <tspan x="58" y="438">&amp; Hyaluronic Acid</tspan>
      </text>
      <text class="body-copy" x="58" y="460" font-size="10.5">30 Servings | 13.500mg per serving</text>

      <g class="benefit-icons">
        <circle class="icon" cx="289" cy="392" r="1.8"/>
        <circle class="icon" cx="296" cy="389" r="1.8"/>
        <circle class="icon" cx="294" cy="396" r="1.8"/>
        <path class="icon" d="M292 411 c-3 4 -4 6 -4 7.5 a4 4 0 0 0 8 0 c0 -1.5 -1 -3.5 -4 -7.5z"/>
        <path class="icon" d="M287 446 c1 -6 5 -8 10 -8 c0 5 -3 9 -10 8z M287 446 l6 -5"/>
        <path class="icon" d="M286 468 q6 -5 12 0 q-6 5 -12 0z"/>
      </g>
      <text class="body-copy" font-size="10.5">
        <tspan x="306" y="395">Low molecular weight</tspan>
        <tspan x="306" y="420">2000 kDa</tspan>
        <tspan x="306" y="445">Unflavored</tspan>
        <tspan x="306" y="470">Sourced from</tspan>
        <tspan x="306" y="480">wild caught fish</tspan>
      </text>

      <text class="body-copy" x="228" y="585" font-size="10" text-anchor="middle">Food Supplement | e 375g</text>
    </g>
  </svg>
</main>
</body>
</html>
```